Business Card Design

We need a design that will also transfer to car decals
We need a design that will speak to the average person needing home and office remodeling
The design should be fresh, exciting, easy to read in a glance and unique
We would like a die-cut tool belt
Bright colors and evenly spaced information

Target Market(s)

Home and business owners
Middle and Upper Income property owners
Families and people with fixer upper homes

Industry/Entity Type

Business

Contact Information for Business Card

Looking for the best Bay Area Handyman? Here I am!
RKW Handyman Services does it all at prices regular people can afford.
Electrical, Plumbing, Carpentry, Remodeling, Fencing, Picture and window placement, Hauling ... and anything else you can imagine!
510-473-2918
Serving the Entire Bay Area
Free Estimates! Call us Today to turn your dreams into reality!

Font styles to use
Serif

Requirements
Must have
• Speaks to the average person
stands out among similar industry cards
Nice to have
• fun, comical, you want to hold on to this card
Should not have
• bland colors
look too crowded

```html
<!DOCTYPE html>
<html lang="en">
<head>
<meta charset="utf-8">
<title>RKW Handyman Services – Business Card</title>
<link href="https://fonts.googleapis.com/css2?family=Dosis:wght@500;600;700;800&display=swap" rel="stylesheet">
<style>
  :root {
    --bg: #ececec;
    --cyan: #14f0f4;
    --black: #0a0a0a;
    --charcoal: #262626;
    --white: #ffffff;
    --ink: #101010;
    --icon-light: #f4f4f4;
    --icon-mid: #d9e6ea;
  }
  * { margin: 0; padding: 0; box-sizing: border-box; }
  html, body { width: 1200px; height: 1000px; overflow: hidden; background: var(--bg); }
  body { position: relative; font-family: "Dosis", sans-serif; }

  .card {
    position: absolute;
    left: 250px;
    width: 700px;
    height: 400px;
    background: var(--cyan);
    overflow: hidden;
    box-shadow: 0 2px 8px rgba(0,0,0,0.18);
  }
  .card--front { top: 70px; }
  .card--back { top: 530px; }

  .card__band { position: absolute; left: 0; top: 0; width: 700px; height: 400px; }

  .band-text {
    position: absolute;
    left: 322px;
    top: 252px;
    transform: translate(-50%, -50%) rotate(-40.4deg);
    white-space: nowrap;
    text-align: center;
    color: var(--white);
    line-height: 1;
  }

  /* front */
  .headline {
    position: absolute; left: 34px; top: 36px;
    font-size: 27px; font-weight: 600; line-height: 1.12;
    text-transform: uppercase; letter-spacing: 0.5px; color: var(--ink);
  }
  .greeting { display: block; font-size: 24px; font-weight: 700; letter-spacing: 1px; margin-bottom: 8px; }
  .brand-name { display: block; font-size: 32px; font-weight: 700; letter-spacing: 1px; text-transform: uppercase; }
  .promise {
    position: absolute; right: 30px; bottom: 34px;
    font-size: 27px; font-weight: 600; line-height: 1.12; text-align: right;
    text-transform: uppercase; letter-spacing: 0.5px; color: var(--ink);
  }
  .trade-icons {
    position: absolute; right: 24px; top: 8px;
    width: 46px; height: 46px; border-radius: 50%;
    background: radial-gradient(circle, var(--icon-light), var(--icon-mid));
  }

  /* back */
  .services {
    position: absolute; left: 34px; top: 36px; list-style: none;
    font-size: 18px; font-weight: 600; line-height: 1.4; color: var(--ink);
  }
  .services__more { padding-left: 6px; }
  .phone__number { display: block; font-size: 58px; font-weight: 800; letter-spacing: 1px; }
  .phone__tagline { display: block; font-size: 17px; font-weight: 600; margin-top: 6px; }
  .coverage {
    position: absolute; right: 30px; bottom: 40px;
    font-size: 21px; font-weight: 600; color: var(--ink);
  }
</style>
</head>
<body>

  <section class="card card--front" aria-label="Business card front">
    <svg class="card__band" viewBox="0 0 700 400" aria-hidden="true">
      <polygon points="581,110 700,110 700,160 522,160" fill="var(--charcoal)"/>
      <polygon points="60,400 460,60 700,60 700,110 581,110 240,400" fill="var(--black)"/>
    </svg>

    <p class="headline">Looking for<br>the best Bay Area<br>Handyman?</p>

    <p class="band-text">
      <span class="greeting">HERE I AM!</span>
      <span class="brand-name">RKW Handyman Services</span>
    </p>

    <p class="promise">Does it all at prices<br>regular people can afford.</p>

    <div class="trade-icons" role="img" aria-label="Trade icons for carpentry, plumbing, home and electrical work"></div>
  </section>

  <section class="card card--back" aria-label="Business card back">
    <svg class="card__band" viewBox="0 0 700 400" aria-hidden="true">
      <polygon points="581,110 700,110 700,160 522,160" fill="var(--charcoal)"/>
      <polygon points="60,400 460,60 700,60 700,110 581,110 240,400" fill="var(--black)"/>
    </svg>

    <ul class="services">
      <li>• Electrical • Plumbing • Carpentry</li>
      <li>• Remodeling • Fencing • Hauling</li>
      <li>• Picture and window placement</li>
      <li class="services__more">...and anything else you can imagine!</li>
    </ul>

    <p class="band-text">
      <span class="phone__number">510-473-2918</span>
      <span class="phone__tagline">Call us Today to turn your dreams into reality!</span>
    </p>

    <p class="coverage">Serving the Entire Bay Area Free Estimates!</p>
  </section>

</body>
</html>
```